Technology company needs an invitation for a Machine Learning Event

We need a invitation design for a technology company called Corvalent. We specialize on IT Services and Consulting and we're scheduling an Event on Machine Learning and Artificial Intelligence. Machine learning is a method of data analysis that automates analytical model building. It is a branch of artificial intelligence based on the idea that systems can learn from data, identify patterns and make decisions with minimal human intervention. It is the result of algorithmic implementations for data analysts to use. So basically, it provides systems the ability to automatically learn and improve from experience without being explicitly programmed to. Machine learning focuses on the development of computer programs that can access data and use it learn for themselves.
Colors
Designer to choose colors to be used in the design.
Look and feel
Each slider illustrates characteristics of the customer's brand and the style your logo design should communicate.

```html
<!DOCTYPE html>
<html lang="en">
<head>
<meta charset="utf-8">
<title>Machine Learning and Artificial Intelligence Event Invitation</title>
<link rel="stylesheet" href="https://fonts.googleapis.com/css2?family=Questrial&display=swap">
<style>
  :root {
    --ink-black: #000000;
    --deep-violet: #1c1128;
    --mid-violet: #3b2650;
    --haze-violet: #6d5a86;
    --spot-glow: #dcebf3;
    --spot-mist: #a9b9c6;
    --teal-type: #63b6ae;
    --teal-beam: rgba(110, 200, 190, 0.55);
  }
  html, body {
    margin: 0;
    padding: 0;
    width: 1200px;
    height: 853px;
    overflow: hidden;
    background: var(--ink-black);
  }
  .invitation {
    position: relative;
    width: 1200px;
    height: 853px;
    overflow: hidden;
    background: var(--ink-black);
    font-family: "Questrial", "Century Gothic", sans-serif;
  }
  .hero-artwork {
    position: absolute;
    inset: 0;
    background:
      radial-gradient(ellipse 300px 240px at 1010px 110px, var(--spot-glow) 0%, rgba(220,235,243,0.6) 45%, rgba(220,235,243,0) 100%),
      radial-gradient(ellipse 520px 420px at 900px 260px, var(--spot-mist) 0%, var(--haze-violet) 40%, var(--mid-violet) 68%, rgba(28,17,40,0) 100%),
      radial-gradient(ellipse 760px 560px at 640px 420px, var(--mid-violet) 0%, var(--deep-violet) 55%, rgba(0,0,0,0) 100%),
      var(--ink-black);
  }
  .light-beam {
    position: absolute;
    left: 180px;
    top: 424px;
    width: 1020px;
    height: 6px;
    background: linear-gradient(90deg, rgba(110,200,190,0) 0%, var(--teal-beam) 55%, rgba(150,220,210,0.8) 85%, rgba(110,200,190,0.3) 100%);
    filter: blur(2px);
  }
  .headline {
    position: absolute;
    left: 0;
    width: 100%;
    margin: 0;
    color: var(--teal-type);
    font-weight: 400;
    font-size: 37px;
    letter-spacing: -1.2px;
    line-height: 1;
    white-space: nowrap;
    text-transform: uppercase;
  }
  .headline span {
    position: absolute;
    transform: translateX(-50%);
  }
  .headline .line-invite { top: 429px; left: 660px; }
  .headline .line-topic { top: 509px; left: 660px; }
  .headline .line-event { top: 588px; left: 666px; }
  .details {
    position: absolute;
    top: 791px;
    color: var(--teal-type);
    font-size: 37px;
    letter-spacing: -1.2px;
    line-height: 1;
    text-transform: uppercase;
  }
  .details.venue { left: 394px; }
  .details.time { left: 786px; }
</style>
</head>
<body>
  <main class="invitation">
    <div class="hero-artwork" role="img" aria-label="Illustration of a robot head in profile wrapped in glowing teal string-art lines, lit by a spotlight from the upper right"></div>
    <div class="light-beam"></div>
    <h1 class="headline">
      <span class="line-invite">You are invited to</span>
      <span class="line-topic">Machine learning and</span>
      <span class="line-event">Artificial intelligence event</span>
    </h1>
    <div class="details venue">Venue:</div>
    <div class="details time">Time:</div>
  </main>
</body>
</html>
```